The name of my company is Tolland Refacing LLC and I would like the sub text to say "Cabinet Refacing and Countertops". Have my name Morris Pelton, Owner / Sales, contact info: Cell: 360-555-0147 / Email: morris.pelton@quillbox.net

Simple, Clean, and Organized. With colors that will appeal to the eye.

Target Market(s)

Houses and Apartments

Industry/Entity Type

Cabinet Refacing

Contact Information for Business Card

Company name and sub text Morris Pelton - Owner / Sales, my cell phone number and email

Requirements
Must have
• Business name, my name / position, and my contact info
Nice to have
• Simple. Organized. Appealing to the eye

```html
<!DOCTYPE html>
<html lang="en">
<head>
<meta charset="UTF-8">
<title>Tolland Refacing LLC – Business Card</title>
<link rel="stylesheet" href="https://fonts.googleapis.com/css2?family=Montserrat:wght@300;400;600;700&family=Poppins:wght@400&display=swap">
<style>
  :root {
    --page-bg: #d4d4d4;
    --card-white: #ffffff;
    --card-black: #000000;
    --brand-blue: #436cb8;
    --brand-blue-light: #5a82c8;
    --slate: #444444;
    --ink: #333333;
    --logo-grey: #bdbdbd;
    --tagline-grey: #5a5a5a;
  }
  * { box-sizing: border-box; margin: 0; padding: 0; }
  html, body {
    width: 1200px; height: 800px; overflow: hidden;
    background: var(--page-bg);
  }
  .sheet {
    width: 1200px; height: 800px;
    display: flex; flex-direction: column; align-items: center; justify-content: center;
    gap: 46px;
  }
  .card {
    position: relative;
    width: 600px; height: 343px;
    border-radius: 22px;
    overflow: hidden;
    border-bottom: 3px solid var(--brand-blue);
    box-shadow: 0 10px 24px rgba(0,0,0,0.22);
  }

  /* Front */
  .card-front { background: var(--card-white); }
  .corner-strip {
    position: absolute; top: 0; right: 0;
    width: 190px; height: 52px;
    background: var(--slate);
  }
  .holder {
    position: absolute; left: 46px; top: 92px;
    font-family: "Montserrat", sans-serif;
  }
  .holder-name {
    font-weight: 600; font-size: 27px; letter-spacing: 1px;
    color: var(--brand-blue); line-height: 1.05;
  }
  .holder-role {
    font-family: "Poppins", sans-serif;
    font-size: 19px; color: var(--ink); line-height: 1.2;
  }
  .contact-band {
    position: absolute; left: 0; top: 196px;
    width: 400px; height: 84px;
    background: var(--brand-blue);
    padding: 12px 0 0 60px;
    font-family: "Montserrat", sans-serif;
    color: #fff;
  }
  .contact-row {
    display: flex; align-items: center; gap: 8px;
    font-size: 19px; line-height: 30px; letter-spacing: 0.3px;
  }
  .contact-row svg { width: 16px; height: 16px; flex: none; }
  .emblem-area {
    position: absolute; left: 388px; top: 74px;
    width: 170px; height: 206px;
    background: linear-gradient(160deg, var(--brand-blue-light), var(--brand-blue));
    clip-path: polygon(20% 0, 100% 0, 100% 100%, 0 100%, 0 55%);
  }

  /* Back */
  .card-back {
    background: var(--card-black);
    display: flex; align-items: center; justify-content: center;
  }
  .brand {
    text-align: center;
    font-family: "Montserrat", sans-serif;
  }
  .brand-line {
    display: flex; align-items: center; justify-content: center; gap: 12px;
  }
  .brand-mark {
    width: 20px; height: 20px; background: var(--brand-blue);
  }
  .brand-name {
    font-weight: 300; font-size: 34px; letter-spacing: 1px;
    color: var(--logo-grey);
  }
  .brand-tagline {
    margin-top: 4px;
    font-weight: 700; font-size: 19px; letter-spacing: 0.5px;
    color: var(--tagline-grey);
  }
</style>
</head>
<body>
<main class="sheet">
  <section class="card card-front">
    <div class="corner-strip"></div>
    <div class="holder">
      <p class="holder-name">MORRIS PELTON</p>
      <p class="holder-role">Owner / Sales</p>
    </div>
    <div class="emblem-area" role="img" aria-label="Brand mountain emblem area"></div>
    <div class="contact-band">
      <p class="contact-row">
        <svg viewBox="0 0 24 24" aria-hidden="true"><path fill="#fff" d="M6.6 10.8a15.1 15.1 0 0 0 6.6 6.6l2.2-2.2a1 1 0 0 1 1-.25 11.4 11.4 0 0 0 3.6.57 1 1 0 0 1 1 1V20a1 1 0 0 1-1 1A17 17 0 0 1 3 4a1 1 0 0 1 1-1h3.5a1 1 0 0 1 1 1c0 1.25.2 2.45.57 3.57a1 1 0 0 1-.25 1z"/></svg>
        360-555-0147
      </p>
      <p class="contact-row">
        <svg viewBox="0 0 24 24" aria-hidden="true"><rect x="2" y="5" width="20" height="14" fill="#fff"/><path d="M2 5l10 8 10-8" fill="none" stroke="#436cb8" stroke-width="2"/></svg>
        morris.pelton@quillbox.net
      </p>
    </div>
  </section>

  <section class="card card-back">
    <div class="brand">
      <div class="brand-line">
        <span class="brand-mark"></span>
        <p class="brand-name">TOLLAND REFACING, LLC</p>
      </div>
      <p class="brand-tagline">Cabinet Refacing and Countertops</p>
    </div>
  </section>
</main>
</body>
</html>
```